Business card design for sustainable building and development company

Need a business card design for a new sustainable building and real estate development company in the San Francisco Bay area. Name of company is "Norvale Advisors, LLC" and we provide "Sustainable building, energy and development services" for residential and non residential projects. We'd like the following colors used but not all area required: green, gray, blue. Design should communicate innovation, professionalism and sustainability. Our current website is www.norvale-advisors.example. Another possible design idea is to have the following listed on the back of the card:
Certified: TRAM QX, Leaf Mark Grader, VOLT Grader, EcoState Examiner, RDQ HX Building Analyst. Its not a must but could be text that could be used for back of card. Overall, we are open to a simple, clean design and or one with more text than usual for a card.

Industry/Entity Type

Real Estate

Contact Information for Business Card

Name on card: Dmitri L. Hasby
Title for Name: Principal + Founder
Phone: 555.418.2096
Email: dhasby@norvale-advisors.example
Website: www.norvale-advisors.example

Also, please add the following for address:
San Francisco, California

Requirements
Nice to have
• If you can integrate the outline of a skyline on the backside of the card and if it looks good, I would like to see the design
Should not have
• a barcode;

```html
<!DOCTYPE html>
<html lang="en">
<head>
<meta charset="utf-8">
<title>Norvale Advisors, LLC — Business Card</title>
<link rel="stylesheet" href="https://fonts.googleapis.com/css2?family=Abel&display=swap">
<style>
  :root {
    --paper: #ffffff;
    --ink: #4a4a4a;
    --rule: #d8d8d8;
    --blue: #339fdb;
    --green: #a2cc3a;
  }
  html, body {
    margin: 0;
    padding: 0;
    width: 1200px;
    height: 678px;
    overflow: hidden;
    background: var(--paper);
  }
  .card {
    position: relative;
    width: 1200px;
    height: 678px;
    background: var(--paper);
    font-family: "Abel", sans-serif;
    color: var(--ink);
  }
  .company-name {
    position: absolute;
    left: 273px;
    top: 136px;
    margin: 0;
    font-size: 78px;
    font-weight: 400;
    line-height: 1;
    letter-spacing: 0.5px;
  }
  .header-rule {
    position: absolute;
    left: 0;
    top: 232px;
    width: 979px;
    height: 17px;
    background: var(--rule);
  }
  .block-blue {
    position: absolute;
    left: 0;
    top: 249px;
    width: 245px;
    height: 280px;
    background: var(--blue);
  }
  .block-green {
    position: absolute;
    left: 0;
    top: 529px;
    width: 245px;
    height: 149px;
    background: var(--green);
  }
  .tagline {
    position: absolute;
    left: 279px;
    top: 262px;
    margin: 0;
    font-size: 48px;
    line-height: 56px;
    font-weight: 400;
  }
</style>
</head>
<body>
  <main class="card">
    <h1 class="company-name">Norvale Advisors, LLC</h1>
    <div class="header-rule"></div>
    <div class="block-blue"></div>
    <div class="block-green"></div>
    <p class="tagline">Sustainable building,<br>energy and development services</p>
  </main>
</body>
</html>
```